New Templates: PowerPoint and Word Template

We need new templates that match our new branding. These documents should have similar look and feels but should be optimized for the specific format:
- PowerPoint template
- Word Document template

Requirements
Must have
• professional, clean, majority of white or off-white background.
Nice to have
• reusable graphics/charts/design elements

```html
<!DOCTYPE html>
<html lang="en">
<head>
<meta charset="utf-8">
<title>Project Title Slide</title>
<link rel="stylesheet" href="https://fonts.googleapis.com/css2?family=Saira:wght@400;600;800&family=Saira+Condensed:ital,wght@1,800&family=Saira+Semi+Condensed:wght@600&display=swap">
<style>
  :root {
    --navy: #0f2a4d;
    --navy-deep: #0b2242;
    --rule: #c9d3df;
    --white: #ffffff;
    --heading-blue: #0e4a8a;
    --body-text: #333333;
    --frame: #dcdcdc;
    --placeholder-text: #c8c8c8;
  }
  html, body {
    margin: 0;
    padding: 0;
    width: 1200px;
    height: 900px;
    overflow: hidden;
    background: var(--white);
  }
  .slide {
    position: relative;
    width: 1200px;
    height: 900px;
    background: var(--white);
    font-family: "Saira", sans-serif;
  }
  .slide-header {
    position: absolute;
    left: 0; top: 0;
    width: 1200px;
    height: 99px;
    background: linear-gradient(180deg, var(--navy) 0%, var(--navy-deep) 100%);
    border-bottom: 2px solid var(--rule);
    box-sizing: border-box;
  }
  .project-title {
    position: absolute;
    left: 33px; top: 16px;
    margin: 0;
    font-family: "Saira Condensed", sans-serif;
    font-style: italic;
    font-weight: 800;
    font-size: 60px;
    line-height: 72px;
    color: var(--white);
    letter-spacing: 0.5px;
  }
  .brand-name {
    position: absolute;
    right: 34px; top: 18px;
    font-family: "Saira", sans-serif;
    font-weight: 800;
    font-size: 46px;
    line-height: 60px;
    color: var(--white);
  }
  .section-heading {
    position: absolute;
    left: 31px; top: 146px;
    margin: 0;
    font-family: "Saira Semi Condensed", sans-serif;
    font-weight: 600;
    font-size: 43px;
    line-height: 52px;
    color: var(--heading-blue);
  }
  .body-copy {
    position: absolute;
    left: 32px; top: 210px;
    width: 635px;
  }
  .body-copy p {
    margin: 0 0 36px;
    font-size: 21.5px;
    line-height: 36px;
    color: var(--body-text);
    text-align: justify;
  }
  .body-copy p.clipped {
    max-height: 108px;
    overflow: hidden;
  }
  .image-slot {
    position: absolute;
    left: 712px;
    width: 438px;
    height: 211px;
    border: 1.5px solid var(--frame);
    border-radius: 4px;
    box-sizing: border-box;
    display: flex;
    align-items: center;
    justify-content: center;
    font-size: 21px;
    color: var(--placeholder-text);
  }
  .image-slot--top { top: 207px; }
  .image-slot--bottom { top: 457px; }
  .slide-footer {
    position: absolute;
    left: 0; top: 828px;
    width: 1200px;
    height: 72px;
    background: linear-gradient(180deg, var(--navy) 0%, var(--navy-deep) 100%);
    color: var(--white);
    font-size: 22px;
  }
  .copyright {
    position: absolute;
    left: 38px; top: 21px;
  }
  .page-number {
    position: absolute;
    right: 30px; top: 21px;
  }
</style>
</head>
<body>
<div class="slide">
  <header class="slide-header">
    <h1 class="project-title">PROJECT TITLE HERE</h1>
    <div class="brand-name">Veritrex</div>
  </header>

  <h2 class="section-heading">Lorem ipsum dolor sit ipsum</h2>

  <section class="body-copy">
    <p>Lorem ipsum dolor sit ipsum Lorem ipsum dolor sit ipsum Lorem ipsum dolor sit ipsum Lorem ipsum dolor sit ipsum lorem ipsum dolor sit ipsum Lorem ipsum dolor sit ipsum Lorem ipsum dolor sit ipsum</p>
    <p>Lorem ipsum dolor sit ipsum Lorem ipsum dolor sit ipsum Lorem ipsum dolor sit ipsum Lorem ipsum dolor sit ipsum lorem ipsum dolor sit ipsum Lorem ipsum dolor sit ipsum Lorem ipsum dolor sit ipsum Lorem ipsum dolor sit ipsum</p>
    <p class="clipped">Lorem ipsum dolor sit ipsum Lorem ipsum dolor sit ipsum Lorem ipsum dolor sit ipsum Lorem ipsum dolor sit ipsum lorem ipsum dolor sit ipsum Lorem ipsum dolor sit ipsum Lorem ipsum dolor sit ipsum Lorem ipsum dolor sit ipsum</p>
  </section>

  <div class="image-slot image-slot--top">IMG HERE</div>
  <div class="image-slot image-slot--bottom">IMG HERE</div>

  <footer class="slide-footer">
    <span class="copyright">Copyright text here</span>
    <span class="page-number">Page : 01</span>
  </footer>
</div>
</body>
</html>
```